Business Card for bespoke luxury cupcakes and cakes
childrens parties, baby showers, seasonal designs, christenings, 3D and 2D designs
Bright & Fun-filled
Tumble Bakes Ltd
London
morvenaltoski@mailnest.co.uk
www.pagelink.co.uk/TumbleBakesLtd

```html
<!DOCTYPE html>
<html lang="en">
<head>
<meta charset="utf-8">
<title>Tumble Bakes Ltd – Business Card</title>
<link rel="stylesheet" href="https://fonts.googleapis.com/css2?family=Arimo:wght@700&display=swap">
<style>
  :root {
    --page-bg: #efede8;
    --card-pink: #ee2a8c;
    --band-white: #ffffff;
    --text-pink: #e0176f;
    --text-white: #ffffff;
    --deco-teal: #7fd3d8;
    --deco-yellow: #f2e66a;
    --deco-orange: #f59a3c;
    --deco-rose: #f7a6c9;
    --logo-dot: #ffd1e6;
  }
  * { margin: 0; padding: 0; box-sizing: border-box; }
  html, body {
    width: 1200px;
    height: 828px;
    overflow: hidden;
    background: var(--page-bg);
  }
  .business-card {
    position: absolute;
    left: 40px;
    top: 40px;
    width: 1120px;
    height: 748px;
    border-radius: 28px;
    background: var(--card-pink);
    overflow: hidden;
    font-family: "Arimo", Arial, sans-serif;
    font-weight: 700;
  }
  .card-shapes {
    position: absolute;
    inset: 0;
    width: 1120px;
    height: 748px;
  }
  .brand-mark {
    position: absolute;
    left: 560px;
    top: 70px;
    display: flex;
    align-items: center;
    gap: 28px;
  }
  .brand-dot {
    width: 96px;
    height: 96px;
    border-radius: 50%;
    background: var(--logo-dot);
    flex: none;
  }
  .brand-name {
    color: var(--text-white);
    font-size: 96px;
    line-height: 0.98;
    letter-spacing: -1px;
  }
  .contact-email {
    position: absolute;
    left: 468px;
    top: 388px;
    color: var(--text-pink);
    font-size: 38px;
    letter-spacing: -0.3px;
  }
  .contact-web {
    position: absolute;
    left: 520px;
    top: 446px;
    color: var(--text-pink);
    font-size: 24px;
  }
  .contact-phone {
    position: absolute;
    right: 60px;
    top: 560px;
    color: var(--text-white);
    font-size: 36px;
    letter-spacing: 0.5px;
  }
</style>
</head>
<body>
  <main class="business-card">
    <svg class="card-shapes" viewBox="0 0 1120 748" aria-hidden="false">
      <defs>
        <linearGradient id="decoGradient" x1="0" y1="0" x2="1" y2="1">
          <stop offset="0" stop-color="var(--deco-teal)"/>
          <stop offset="0.35" stop-color="var(--deco-rose)"/>
          <stop offset="0.65" stop-color="var(--deco-yellow)"/>
          <stop offset="1" stop-color="var(--deco-orange)"/>
        </linearGradient>
      </defs>
      <path class="decorative-swirls" role="img"
            aria-label="Colourful abstract swirl and paisley pattern in teal, yellow, orange and pink"
            fill="url(#decoGradient)" opacity="0.9"
            d="M0 150 C 120 110 260 130 330 220 C 400 310 300 380 340 460
               C 380 540 300 620 240 680 C 200 720 140 748 90 748 L 0 748 Z"/>
      <polygon class="contact-band" fill="var(--band-white)"
               points="470,352 1120,352 1120,512 330,512"/>
    </svg>

    <div class="brand-mark">
      <span class="brand-dot"></span>
      <span class="brand-name">Tumble<br>Bakes</span>
    </div>

    <p class="contact-email">morvenaltoski@mailnest.co.uk</p>
    <p class="contact-web">www.pagelink.co.uk/TumbleBakesLtd</p>
    <p class="contact-phone">+44-7700-900-418</p>
  </main>
</body>
</html>
```